" buscamos elaborar produtos saudáveis, isentos de glúten, lactose e açúcar. E utilizando ingredientes benéficos a nossa saúde, como fibra e gorduras boas (insaturadas). "

```html
<!DOCTYPE html>
<html lang="pt-BR">
<head>
<meta charset="utf-8">
<title>Semente Viva – Cartão de visita</title>
<link href="https://fonts.googleapis.com/css2?family=Comfortaa:wght@600;700&family=Open+Sans:wght@400;600&display=swap" rel="stylesheet">
<style>
  :root {
    --bg: #ecebe6;
    --card-white: #ffffff;
    --green: #6f9c1f;
    --green-dark: #5c8a14;
    --green-light: #7fae28;
    --orange: #e9792a;
    --yellow: #f2b233;
    --text-white: #ffffff;
    --shadow: rgba(0, 0, 0, 0.18);
  }
  * { box-sizing: border-box; margin: 0; padding: 0; }
  html, body { width: 1200px; height: 1200px; overflow: hidden; }
  body {
    background: var(--bg);
    font-family: "Open Sans", Arial, sans-serif;
    position: relative;
  }
  .card {
    position: absolute;
    left: 150px;
    width: 900px;
    height: 500px;
    border-radius: 22px;
    box-shadow: 0 14px 34px var(--shadow);
    overflow: hidden;
  }
  .card-front { top: 70px; background: var(--card-white); }
  .card-back {
    top: 630px;
    background: radial-gradient(ellipse at 35% 30%, var(--green-light), var(--green) 55%, var(--green-dark));
  }

  .brand {
    display: flex;
    align-items: center;
    gap: 22px;
    font-family: "Comfortaa", "Varela Round", sans-serif;
    font-weight: 700;
    white-space: nowrap;
  }
  .brand-dot { border-radius: 50%; flex: none; }

  .card-front .brand {
    position: absolute;
    left: 50%; top: 50%;
    transform: translate(-50%, -50%);
    flex-direction: column;
    gap: 26px;
    font-size: 64px;
    color: var(--green);
  }
  .card-front .brand-dot {
    width: 130px; height: 130px;
    background: radial-gradient(circle at 40% 40%, var(--yellow), var(--orange) 70%);
  }

  .card-back .brand {
    position: absolute;
    left: 86px; top: 120px;
    flex-direction: column;
    gap: 16px;
    font-size: 38px;
    color: var(--text-white);
  }
  .card-back .brand-dot { width: 78px; height: 78px; background: var(--text-white); }

  .holder {
    position: absolute;
    left: 470px; top: 92px;
    font-size: 29px;
    font-weight: 600;
    color: var(--text-white);
  }
  .contact-list {
    position: absolute;
    left: 470px; top: 178px;
    list-style: none;
    color: var(--text-white);
    font-size: 22px;
    line-height: 1.22;
  }
  .contact-list li { display: flex; align-items: flex-start; gap: 14px; }
  .contact-list svg { width: 20px; height: 20px; flex: none; margin-top: 4px; fill: var(--text-white); }
  .contact-list .sub { padding-left: 34px; display: block; }

  .accent-band {
    position: absolute;
    left: 0; right: 0; bottom: 0;
    height: 44px;
    background: linear-gradient(90deg, var(--orange), var(--yellow));
    border-radius: 30px 30px 0 0;
  }
</style>
</head>
<body>

<section class="card card-front" aria-label="Frente do cartão">
  <div class="brand">
    <span class="brand-dot"></span>
    <span class="brand-name">Semente Viva</span>
  </div>
</section>

<section class="card card-back" aria-label="Verso do cartão">
  <div class="brand">
    <span class="brand-dot"></span>
    <span class="brand-name">Semente Viva</span>
  </div>

  <h1 class="holder">Lívia Moraes Prado</h1>

  <ul class="contact-list">
    <li>
      <svg viewBox="0 0 20 20" aria-hidden="true"><path d="M10 1a6 6 0 0 0-6 6c0 4.5 6 12 6 12s6-7.5 6-12a6 6 0 0 0-6-6zm0 8.3A2.3 2.3 0 1 1 10 4.7a2.3 2.3 0 0 1 0 4.6z"/></svg>
      <span>Rua Aurora, 215 Centro</span>
    </li>
    <li><span class="sub">Vila Nova SP</span></li>
    <li>
      <svg viewBox="0 0 20 20" aria-hidden="true"><path d="M5 2l3 4-2 2c1 2.5 3.5 5 6 6l2-2 4 3-2 3C8 18 2 12 2 4z"/></svg>
      <span>+55 11 2000-1111</span>
    </li>
    <li>
      <svg viewBox="0 0 20 20" aria-hidden="true"><path d="M6 1h8a1.5 1.5 0 0 1 1.5 1.5v15A1.5 1.5 0 0 1 14 19H6a1.5 1.5 0 0 1-1.5-1.5v-15A1.5 1.5 0 0 1 6 1zm0 3v11h8V4zm4 12.2a1 1 0 1 0 0 2 1 1 0 0 0 0-2z"/></svg>
      <span>+55 11 9000-0000</span>
    </li>
    <li>
      <svg viewBox="0 0 20 20" aria-hidden="true"><path d="M10 1a9 9 0 1 0 4.5 16.8l-.9-1.6A7.2 7.2 0 1 1 17.2 10v1a1.6 1.6 0 0 1-3.2 0V6h-1.7v.8A4.3 4.3 0 1 0 13 13.6a3.4 3.4 0 0 0 6-2.6V10a9 9 0 0 0-9-9zm0 11.5a2.5 2.5 0 1 1 0-5 2.5 2.5 0 0 1 0 5z"/></svg>
      <span>livia@sementeviva.com</span>
    </li>
    <li>
      <svg viewBox="0 0 20 20" aria-hidden="true"><path d="M10 1a9 9 0 1 0 0 18 9 9 0 0 0 0-18zm6.9 8h-3a14 14 0 0 0-1.2-5.6A7.1 7.1 0 0 1 16.9 9zM10 2.9c.9 1.3 1.7 3.5 1.9 6.1H8.1c.2-2.6 1-4.8 1.9-6.1zM7.3 3.4A14 14 0 0 0 6.1 9h-3a7.1 7.1 0 0 1 4.2-5.6zM3.1 11h3a14 14 0 0 0 1.2 5.6A7.1 7.1 0 0 1 3.1 11zm6.9 6.1c-.9-1.3-1.7-3.5-1.9-6.1h3.8c-.2 2.6-1 4.8-1.9 6.1zm2.7-.5a14 14 0 0 0 1.2-5.6h3a7.1 7.1 0 0 1-4.2 5.6z"/></svg>
      <span>www.sementeviva.com</span>
    </li>
  </ul>

  <div class="accent-band"></div>
</section>

</body>
</html>
```